Professional looking Unforgettable Truck Wrap Design

We are looking for a wrap design for a growing landscape company. We just purchased new trucks and are looking to use our logo in the best way possible so show off who we are and what we do. We want it to be unforgettable and when someone sees our trucks, they know who we are without having to read our name.
We like the colors in our logo, we are more leaning towards larger logos on the sides of the vehicle, and a tailgate logo as well, and not really the full wraps, but maybe open to full wraps.

We are a full service landscape company located in Salt Lake City, Ut, we offer anything from Maintenance, to installation and sprinkler repair.

The trucks we will be getting, are 2021 Varnold 7200 XT crew cabs
we will also have 2021 Varny Tamborine crew cab trucks that I need logos on as well.

We would like to have our phone Number and Website listed on the truck as well as our USDOT # See below in the must haves for the information.

Sick

Industry/Entity Type

Landscaping

Requirements
Must have
• good flow on the truck
bold looking
Clear information

Phone Number 801-555-0182
Website www.fernridgeyardworks.com
USDOT #4817260
Nice to have
• I have uploaded an image of a trailer we currently have, it has our old logo, but we really like the landscape design background so maybe if we could use something similar.

```html
<!DOCTYPE html>
<html lang="en">
<head>
<meta charset="utf-8">
<title>Fernridge Truck Wrap Layout</title>
<link rel="stylesheet" href="https://fonts.googleapis.com/css2?family=Poppins:wght@500;600;700&family=Montserrat:wght@600;700&display=swap">
<style>
  :root {
    --canvas: #ffffff;
    --silver: #eef0f2;
    --brand-blue: #1f6fb7;
    --charcoal: #4a4b4e;
    --ink: #3a3b3d;
    --white: #ffffff;
    --grey-text: #7d7f82;
  }
  html, body {
    margin: 0;
    padding: 0;
    width: 1200px;
    height: 1200px;
    overflow: hidden;
    background: var(--canvas);
  }
  .wrap-sheet {
    position: relative;
    width: 1200px;
    height: 1200px;
  }
  .wrap-side {
    position: absolute;
    left: 50px;
    width: 1100px;
    height: 340px;
  }
  .wrap-side--driver { top: 150px; }
  .wrap-side--passenger { top: 700px; }
  .panel-base { fill: url(#silverFade); }
  .band-blue { fill: var(--brand-blue); }
  .band-charcoal { fill: var(--charcoal); }
  .mark-spot {
    fill: none;
    stroke: var(--brand-blue);
    stroke-width: 10;
  }
  .brand-name {
    font-family: "Poppins", sans-serif;
    font-weight: 600;
    fill: var(--brand-blue);
    letter-spacing: 1px;
  }
  .brand-tagline {
    font-family: "Poppins", sans-serif;
    font-weight: 500;
    fill: var(--grey-text);
  }
  .web-address {
    font-family: "Poppins", sans-serif;
    font-weight: 600;
  }
  .phone {
    font-family: "Montserrat", sans-serif;
    font-weight: 700;
  }
  .usdot {
    font-family: "Montserrat", sans-serif;
    font-weight: 700;
  }
</style>
</head>
<body>
<main class="wrap-sheet">

  <!-- Driver side: front of vehicle at left -->
  <svg class="wrap-side wrap-side--driver" viewBox="0 0 1100 340" role="group" aria-label="Driver side wrap layout">
    <defs>
      <linearGradient id="silverFade" x1="0" y1="0" x2="0" y2="1">
        <stop offset="0" stop-color="#f6f7f8"/>
        <stop offset="1" stop-color="#dfe2e5"/>
      </linearGradient>
    </defs>
    <rect class="panel-base" x="0" y="0" width="1100" height="340" rx="18"/>
    <polygon class="band-blue" points="110,160 500,128 500,137 110,169"/>
    <circle class="mark-spot" cx="580" cy="72" r="52"/>
    <polygon class="band-blue" points="250,300 640,268 600,340 250,340"/>
    <polygon class="band-charcoal" points="615,340 655,272 1100,218 1100,340"/>
    <polygon class="band-blue" points="650,258 1100,196 1100,210 656,270"/>
    <text class="brand-name" x="262" y="224" font-size="62">FERNRIDGE</text>
    <text class="brand-tagline" x="264" y="256" font-size="14" letter-spacing="4">LAWN CARE AND LANDSCAPE</text>
    <text class="web-address" x="285" y="327" font-size="20" fill="var(--white)">www.fernridgeyardworks.com</text>
    <text class="phone" x="690" y="150" font-size="42" fill="var(--ink)">801-555-0182</text>
    <text class="usdot" x="965" y="268" font-size="16" fill="var(--white)">USDOT</text>
    <text class="usdot" x="965" y="290" font-size="16" fill="var(--white)">#4817260</text>
  </svg>

  <!-- Passenger side: front of vehicle at right -->
  <svg class="wrap-side wrap-side--passenger" viewBox="0 0 1100 340" role="group" aria-label="Passenger side wrap layout">
    <rect class="panel-base" x="0" y="0" width="1100" height="340" rx="18"/>
    <polygon class="band-blue" points="0,20 370,20 450,260 0,230"/>
    <polygon class="band-charcoal" points="0,230 450,260 420,340 0,340"/>
    <polygon class="band-blue" points="420,340 450,262 830,255 830,340"/>
    <polygon class="band-charcoal" points="610,244 1100,232 1100,240 612,252"/>
    <circle class="mark-spot" cx="510" cy="160" r="72" style="stroke: var(--charcoal)"/>
    <text class="phone" x="60" y="110" font-size="42" fill="var(--white)">801-555-0182</text>
    <text class="usdot" x="30" y="272" font-size="14" fill="var(--white)">USDOT #4817260</text>
    <text class="brand-name" x="620" y="168" font-size="42">FERNRIDGE</text>
    <text class="brand-tagline" x="622" y="190" font-size="11" letter-spacing="3">LAWN CARE AND LANDSCAPE</text>
    <text class="web-address" x="620" y="222" font-size="15" fill="var(--ink)">www.fernridgeyardworks.com</text>
  </svg>

</main>
</body>
</html>
```